Instagram background for quotes

We need a 1080x1080 background for instagram. I use the Phonto app to put text over the image.

We create motivating and inspiring messages for our followers on IG.

Our brands message is, "Mediocre thinking leads to mediocre results. Get Mission - Get Motivated - Get Moving
https://www.example-social.test/steel_resolve_co/

We would like to move away from the rustic look and have a gloss black background with the goal of using text that is cleaner to match the SR in the logo.

I see the design remaining fairly close to what it is now with the logo at the top. I like the quotes on this brand here, https://www.example-social.test/talkwithtycoons/?hl=en. I see this being built into our new background with the quotations being aggressive to match the wings in our logo.

Here is another brand we like - https://www.example-social.test/boomboomdrive/

I've attached the files I was given by the logo designer who has disappeared. I am hoping what is there will suffice.

Target Market(s)

24-34 year old males

Industry/Entity Type

Quotes

Colors
000000
ffffff

Requirements
Must have
• Provided Logo without text
Nice to have
• Aggressive looking quotes to match wings
• Watermark logo in background

```html
<!DOCTYPE html>
<html lang="en">
<head>
<meta charset="utf-8">
<title>SR Quote Background</title>
<link rel="stylesheet" href="https://fonts.googleapis.com/css2?family=Teko:wght@600&display=swap">
<style>
  :root {
    --ink: #000000;
    --paper: #ffffff;
    --watermark: #161616;
    --texture: #2a2a2a;
  }
  * { box-sizing: border-box; margin: 0; padding: 0; }
  html, body {
    width: 1200px;
    height: 1200px;
    overflow: hidden;
    background: var(--ink);
  }
  .canvas {
    position: relative;
    width: 1200px;
    height: 1200px;
    background: var(--ink);
    overflow: hidden;
    font-family: "Teko", "Arial Narrow", sans-serif;
  }
  .side-texture {
    position: absolute;
    top: 280px;
    width: 140px;
    height: 620px;
    background: linear-gradient(180deg, var(--ink) 0%, var(--texture) 30%, var(--texture) 70%, var(--ink) 100%);
  }
  .side-texture--left { left: 0; }
  .side-texture--right { right: 0; }
  .watermark-name {
    position: absolute;
    left: 0;
    right: 0;
    top: 250px;
    text-align: center;
    font-weight: 600;
    font-size: 720px;
    line-height: 1;
    color: var(--watermark);
    letter-spacing: 10px;
  }
  .frame {
    position: absolute;
    left: 78px;
    top: 78px;
    width: 1040px;
    height: 1043px;
    border: 6px solid var(--paper);
  }
  .brand-mark {
    position: absolute;
    left: 380px;
    top: 20px;
    width: 440px;
    height: 180px;
    background: var(--ink);
    display: flex;
    align-items: center;
    justify-content: center;
    font-weight: 600;
    font-size: 170px;
    line-height: 1;
    color: var(--paper);
    letter-spacing: 6px;
    padding-top: 24px;
  }
  .quote-mark {
    position: absolute;
  }
  .quote-mark--open { left: 44px; top: 214px; width: 98px; height: 146px; }
  .quote-mark--close { left: 1054px; top: 848px; width: 96px; height: 148px; }
</style>
</head>
<body>
  <main class="canvas">
    <div class="side-texture side-texture--left" role="img" aria-label="Faint grey textured wing feathers fading into the black background"></div>
    <div class="side-texture side-texture--right" role="img" aria-label="Faint grey textured wing feathers fading into the black background"></div>

    <div class="watermark-name" aria-hidden="true">SR</div>

    <div class="frame"></div>

    <div class="brand-mark">SR</div>

    <svg class="quote-mark quote-mark--open" viewBox="0 0 98 146" aria-hidden="true">
      <g fill="var(--paper)" stroke="var(--ink)" stroke-width="7" stroke-linejoin="miter">
        <polygon points="6,6 40,6 46,40 34,138 20,92 14,48"/>
        <polygon points="50,14 86,14 92,50 80,140 66,98 58,54"/>
      </g>
    </svg>

    <svg class="quote-mark quote-mark--close" viewBox="0 0 96 148" aria-hidden="true">
      <g fill="var(--paper)" stroke="var(--ink)" stroke-width="7" stroke-linejoin="miter">
        <polygon points="18,8 30,52 36,96 40,132 8,132 4,98"/>
        <polygon points="62,14 76,58 82,102 88,140 54,140 48,104"/>
      </g>
    </svg>
  </main>
</body>
</html>
```